CopperWren Works, LLC Corporate Web Site

The goal of this web site is simple. To provide an information and corporate information site for people who click on company links from other web sites. Put simply, this web site is primarily a brochure web site for the parent business. It will contain information about the company and our products with links to those products. It will be designed as a small web site but scalable as we add more products and services to our repertoire.

Please see the PDF in the uploaded files/media for more information on colors and basic guidelines, but be creative for sure.

Target Market(s)

General

Industry/Entity Type

Technology, Software

Coding

Coded - Design and coding required

Font styles to use
Other font styles liked:
• Goliath, Roboto

Colors
FFC000
F8CF3A
FAE287
FDF2CF
FEFAEE

Requirements
Must have
• Home page template, interior template, News/Press release template
Nice to have
• Searchable
Should not have
• carousels, one-page design

```html
<!DOCTYPE html>
<html lang="en">
<head>
<meta charset="utf-8">
<title>About us – CopperWren Works</title>
<link href="https://fonts.googleapis.com/css2?family=Plus+Jakarta+Sans:wght@400;500;600;700;800&display=swap" rel="stylesheet">
<style>
:root{
  --ink:#121212;
  --body:#555a66;
  --purple:#7f86c4;
  --orange:#f7941d;
  --navy:#0f0e22;
  --white:#ffffff;
}
*{box-sizing:border-box;margin:0;padding:0}
html,body{width:1200px;height:3175px;overflow:hidden;background:var(--white)}
body{position:relative;font-family:"Plus Jakarta Sans",sans-serif;color:var(--ink)}
.abs{position:absolute}

/* header */
.hero-bg{position:absolute;left:0;top:0;width:1200px;height:530px}
.nav{position:absolute;left:85px;top:14px;width:1027px;height:106px;background:var(--white);
  clip-path:polygon(14px 0,100% 0,calc(100% - 16px) 100%,0 100%);border-radius:10px}
.nav-mail{position:absolute;left:885px;top:14px;width:227px;height:40px;background:var(--purple);
  clip-path:polygon(6px 0,100% 0,calc(100% - 4px) 100%,0 100%);border-radius:0 0 0 10px;
  color:var(--white);font-weight:600;font-size:13px;display:flex;align-items:center;padding-left:20px;gap:10px;white-space:nowrap}
.brand{position:absolute;left:121px;top:54px;display:flex;align-items:center;gap:8px;font-weight:800;font-size:20px;color:var(--orange);white-space:nowrap}
.brand i{width:13px;height:13px;border-radius:50%;background:var(--orange);display:block}
.menu{position:absolute;top:76px;font-size:16px;font-weight:500;color:var(--ink);white-space:nowrap}
.menu.active{color:var(--purple)}
.hero-title{position:absolute;left:85px;top:188px;font-size:58px;font-weight:800;color:var(--white);letter-spacing:-1px}
.hero-text{position:absolute;left:85px;top:278px;width:420px;font-size:17.5px;line-height:27.5px;color:var(--white);font-weight:500}

/* intro */
.photo{position:absolute}
.intro-h{position:absolute;left:620px;top:592px;font-size:36px;line-height:46px;font-weight:800;width:470px;letter-spacing:-.3px}
.intro-p{position:absolute;left:620px;width:498px;font-size:17.5px;line-height:27.5px;color:var(--body)}

/* values */
.sec-h{position:absolute;left:0;width:1200px;text-align:center;font-size:38px;font-weight:800}
.sec-sub{position:absolute;left:0;width:1200px;text-align:center;font-size:17.5px;line-height:27.5px;color:var(--body)}
.card{position:absolute;top:1376px;width:356px;height:357px;text-align:center;
  filter:drop-shadow(0 16px 26px rgba(20,20,50,.09))}
.card-shape{position:absolute;left:0;top:0;width:100%;height:100%;background:var(--white);
  clip-path:polygon(36px 0,100% 0,calc(100% - 36px) 100%,0 100%);border-radius:6px}
.card svg{position:absolute;left:50%;top:40px;transform:translateX(-50%)}
.card h3{position:absolute;left:0;top:133px;width:100%;font-size:20px;font-weight:800}
.card p{position:absolute;top:168px;left:50%;transform:translateX(-50%);width:260px;font-size:16px;line-height:27.5px;color:var(--body)}
.card .bar{position:absolute;top:305px;left:50%;transform:translateX(-50%);width:126px;height:4px;
  background:linear-gradient(90deg,var(--purple) 50%,var(--orange) 50%)}

/* mission */
.mission-h{position:absolute;left:85px;top:1958px;font-size:38px;font-weight:800}
.mission-p{position:absolute;left:85px;top:2014px;width:480px;font-size:17.5px;line-height:27.5px;color:var(--body)}
.item{position:absolute;display:flex;align-items:center;gap:10px;font-size:18px;color:var(--body);white-space:nowrap}
.item svg{flex:none}
.btn{position:absolute;left:85px;top:2353px;width:217px;height:52px;background:var(--orange);color:var(--white);
  clip-path:polygon(6px 0,100% 0,calc(100% - 6px) 100%,0 100%);border-radius:4px;
  font-weight:700;font-size:15px;display:flex;align-items:center;justify-content:center;gap:18px}

/* footer */
.footer-bg{position:absolute;left:0;top:2580px;width:1200px;height:595px}
.f-h{position:absolute;top:2720px;font-size:19px;font-weight:800;color:var(--orange)}
.f-link{position:absolute;left:85px;font-size:17.5px;color:var(--white);font-weight:500}
.f-icon{position:absolute;left:368px;width:52px;height:52px;border:1.5px solid rgba(255,255,255,.35);border-radius:50%;
  display:flex;align-items:center;justify-content:center}
.f-label{position:absolute;left:441px;font-size:15px;font-weight:700;color:var(--purple)}
.f-val{position:absolute;left:441px;font-size:18px;color:var(--white);font-weight:500;white-space:nowrap}
.f-news{position:absolute;left:787px;top:2760px;width:330px;font-size:17.5px;line-height:27.5px;color:var(--white);font-weight:500}
.f-input{position:absolute;left:788px;top:2845px;width:270px;height:50px;background:#1b1a33;color:#6f6f83;font-size:15px;
  display:flex;align-items:center;padding-left:20px}
.f-send{position:absolute;left:1057px;top:2845px;width:57px;height:50px;background:var(--orange);display:flex;align-items:center;justify-content:center}
.social{position:absolute;top:2938px;width:52px;height:52px;border-radius:50%;background:var(--purple);display:flex;align-items:center;justify-content:center}
.social i{width:10px;height:10px;border-radius:50%;background:var(--white);display:block}
.rule{position:absolute;left:85px;top:3089px;width:1029px;height:1px;background:rgba(255,255,255,.12)}
.copy{position:absolute;left:0;top:3119px;width:1200px;text-align:center;color:var(--white);font-size:15.5px;font-weight:500}
</style>
</head>
<body>

<svg class="hero-bg" viewBox="0 0 1200 530" aria-hidden="true">
  <defs>
    <linearGradient id="heroGrad" x1="0" y1="0" x2="1" y2="0.4">
      <stop offset="0" stop-color="#0b1a33"/>
      <stop offset="0.45" stop-color="#123a5e"/>
      <stop offset="1" stop-color="#3a7ba6"/>
    </linearGradient>
  </defs>
  <polygon points="0,0 1200,0 1200,400 40,505 0,474" fill="#7f86c4"/>
  <rect role="img" aria-label="Photo of a developer working at a computer with code overlay" x="0" y="0" width="1200" height="480" fill="url(#heroGrad)" style="clip-path:polygon(0 0,100% 0,100% 83.3%,0 100%)"/>
  <polygon points="0,480 1200,400 1200,530 0,530" fill="#ffffff"/>
  <polygon points="0,472 40,505 1200,400 1200,402 44,522 0,488" fill="#7f86c4"/>
</svg>

<div class="nav"></div>
<div class="nav-mail">
  <svg width="18" height="14" viewBox="0 0 20 15"><rect x="1" y="1" width="18" height="13" rx="2" fill="none" stroke="#fff" stroke-width="2"/><path d="M2 2l8 6 8-6" fill="none" stroke="#fff" stroke-width="2"/></svg>
  hello@copperwrenworks.com
</div>
<div class="brand"><i></i>CopperWren Works</div>
<span class="menu" style="left:351px">Home</span>
<span class="menu active" style="left:435px">About</span>
<span class="menu" style="left:522px">Products</span>
<span class="menu" style="left:632px">Projects</span>
<span class="menu" style="left:735px">Contributions</span>
<span class="menu" style="left:887px">News
  <svg width="9" height="6" viewBox="0 0 9 6"><path d="M1 1l3.5 3.5L8 1" fill="none" stroke="#121212" stroke-width="1.8"/></svg></span>
<span class="menu" style="left:981px">Privacy</span>

<h1 class="hero-title">About us</h1>
<p class="hero-text">Lorem ipsum dolor sit amet consectetur adis pisicing elit, sed do eiusmod tempor incidi it dunt ut labore et dolore magna aliqua utter enim ad minim veniam sed.</p>

<div class="photo" role="img" aria-label="Photo of a smiling developer at his desk"
  style="left:85px;top:601px;width:424px;height:486px;background:linear-gradient(135deg,#2c4a63,#5d7f96 55%,#8ba3b3);clip-path:polygon(8% 0,100% 0,92% 100%,0 100%);border-radius:6px"></div>
<div class="photo" aria-hidden="true"
  style="left:338px;top:909px;width:217px;height:220px;background:#fff;clip-path:polygon(10% 0,100% 0,90% 100%,0 100%)"></div>
<div class="photo" role="img" aria-label="Photo of a smiling woman wearing glasses"
  style="left:344px;top:915px;width:207px;height:210px;background:linear-gradient(135deg,#8c9aa6,#c9b39a 50%,#4e5a6a);clip-path:polygon(10% 0,100% 0,90% 100%,0 100%)"></div>

<h2 class="intro-h">We are best in software &amp; applications development</h2>
<p class="intro-p" style="top:742px">Exercitation ullamco laboris nisi ut aliquip ex ea comodo consequa duis aute irure dolor in reprehenderit in vol ptate velit esse cillum dolore eu fugiat nulla pariatur.</p>
<p class="intro-p" style="top:852px">Duis aute irure dolor in reprehenderit in voluptate velit esse cillum dolore eu fugiat nulla pariatur. Excepteur sint occa ecat cupidatat non proident, sunt.</p>
<p class="intro-p" style="top:961px">Excepteur sint occaecat cupidatat non proident, sunte in culpa qui officia deserunt mollit anim id est laborius um ed ut perspiciatis unde omnis iste natus.</p>

<h2 class="sec-h" style="top:1214px">Core Values</h2>
<p class="sec-sub" style="top:1267px">Exercitation ullamco laboris nisi ut aliquip ex ea comodo<br>consequa duis aute irure dolor in reprehenderit</p>

<div class="card" style="left:85px">
  <div class="card-shape"></div>
  <svg width="88" height="62" viewBox="0 0 88 62" fill="none" stroke="#7f86c4" stroke-width="2.5">
    <circle cx="20" cy="14" r="8"/><circle cx="44" cy="11" r="9"/><circle cx="68" cy="14" r="8"/>
    <path d="M4 40c0-9 7-14 16-14M84 40c0-9-7-14-16-14M28 36c0-10 7-15 16-15s16 5 16 15"/>
    <path d="M44 34l11 4v8c0 7-5 11-11 14-6-3-11-7-11-14v-8z"/>
    <path d="M39 46l4 4 7-7" stroke="#f7941d"/>
  </svg>
  <h3>Integrity</h3>
  <p>Exercitation ullamco laboris ut nisi ut aliquip ex ea comodop consequa duis aute irure sedi ut dolor in reprehenderit.</p>
  <div class="bar"></div>
</div>
<div class="card" style="left:422px">
  <div class="card-shape"></div>
  <svg width="80" height="70" viewBox="0 0 80 70" fill="none" stroke="#7f86c4" stroke-width="2.5">
    <path d="M40 2v7M30 5l3 6M50 5l-3 6" stroke="#f7941d"/>
    <circle cx="26" cy="22" r="6"/><circle cx="40" cy="18" r="6"/><circle cx="54" cy="22" r="6"/>
    <path d="M4 40l14-10 6 4M76 40L62 30l-6 4"/>
    <path d="M4 40v22h10l12-10 8 6 6-4 10 8 8-6 8 6h10V40"/>
    <path d="M24 44l12-8 8 4 12-2"/>
  </svg>
  <h3>Build Relationships</h3>
  <p>Exercitation ullamco laboris ut nisi ut aliquip ex ea comodop consequa duis aute irure sedi ut dolor in reprehenderit.</p>
  <div class="bar"></div>
</div>
<div class="card" style="left:759px">
  <div class="card-shape"></div>
  <svg width="74" height="70" viewBox="0 0 74 70" fill="none" stroke="#7f86c4" stroke-width="2.5">
    <circle cx="10" cy="8" r="5"/><path d="M10 14v14l-6 10M10 22l10-4M10 28l8 8"/>
    <circle cx="52" cy="18" r="10" stroke="#f7941d"/><circle cx="52" cy="18" r="4" stroke="#f7941d"/>
    <rect x="4" y="52" width="10" height="16"/><rect x="20" y="44" width="10" height="24"/>
    <rect x="36" y="40" width="10" height="28"/><rect x="52" y="36" width="10" height="32"/>
    <path d="M64 34v34"/>
  </svg>
  <h3>Working Hard</h3>
  <p>Exercitation ullamco laboris ut nisi ut aliquip ex ea comodop consequa duis aute irure sedi ut dolor in reprehenderit.</p>
  <div class="bar"></div>
</div>

<h2 class="mission-h">Our Mission</h2>
<p class="mission-p">Exercitation ullamco laboris nisi ut aliquip ex eacom odo consequa duis aute irure dolor in reprehen derit in vol ptate velit esse cillum dolore eu fugiat nulla se Duis aute irure dolor in reprehe nderit in voluptate velit esse cillum dolore eu fugiat nulla.</p>

<div class="item" style="left:85px;top:2181px"><svg width="16" height="16" viewBox="0 0 16 16"><circle cx="8" cy="8" r="8" fill="#f7941d"/><path d="M4 8h7M8 5l3 3-3 3" fill="none" stroke="#fff" stroke-width="1.6"/></svg>cillum dolore eu fug</div>
<div class="item" style="left:334px;top:2181px"><svg width="16" height="16" viewBox="0 0 16 16"><circle cx="8" cy="8" r="8" fill="#f7941d"/><path d="M4 8h7M8 5l3 3-3 3" fill="none" stroke="#fff" stroke-width="1.6"/></svg>Rure dolor in reprehe</div>
<div class="item" style="left:85px;top:2232px"><svg width="16" height="16" viewBox="0 0 16 16"><circle cx="8" cy="8" r="8" fill="#f7941d"/><path d="M4 8h7M8 5l3 3-3 3" fill="none" stroke="#fff" stroke-width="1.6"/></svg>cillum dolore eu fug</div>
<div class="item" style="left:334px;top:2232px"><svg width="16" height="16" viewBox="0 0 16 16"><circle cx="8" cy="8" r="8" fill="#f7941d"/><path d="M4 8h7M8 5l3 3-3 3" fill="none" stroke="#fff" stroke-width="1.6"/></svg>Rure dolor in reprehe</div>
<div class="item" style="left:85px;top:2282px"><svg width="16" height="16" viewBox="0 0 16 16"><circle cx="8" cy="8" r="8" fill="#f7941d"/><path d="M4 8h7M8 5l3 3-3 3" fill="none" stroke="#fff" stroke-width="1.6"/></svg>cillum dolore eu fug</div>
<div class="item" style="left:334px;top:2282px"><svg width="16" height="16" viewBox="0 0 16 16"><circle cx="8" cy="8" r="8" fill="#f7941d"/><path d="M4 8h7M8 5l3 3-3 3" fill="none" stroke="#fff" stroke-width="1.6"/></svg>Rure dolor in reprehe</div>

<div class="btn">View Products
  <svg width="24" height="12" viewBox="0 0 24 12"><path d="M1 6h21M17 1l5 5-5 5" fill="none" stroke="#fff" stroke-width="2"/></svg>
</div>

<svg class="abs" style="left:590px;top:1880px" width="540" height="500" viewBox="0 0 540 500" aria-hidden="true">
  <defs>
    <linearGradient id="arcGrad" x1="0" y1="0" x2="1" y2="1">
      <stop offset="0" stop-color="#fdf2cf" stop-opacity="0"/>
      <stop offset="0.5" stop-color="#fae0b0"/>
      <stop offset="1" stop-color="#f7c98a"/>
    </linearGradient>
    <linearGradient id="circleGrad" x1="0" y1="0" x2="1" y2="1">
      <stop offset="0" stop-color="#17344f"/>
      <stop offset="0.55" stop-color="#3b7391"/>
      <stop offset="1" stop-color="#7fb0c4"/>
    </linearGradient>
  </defs>
  <circle cx="290" cy="249" r="226" fill="url(#arcGrad)"/>
  <circle cx="304" cy="239" r="222" fill="#ffffff"/>
  <circle role="img" aria-label="Photo of a developer with headphones typing code" cx="304" cy="239" r="219" fill="url(#circleGrad)"/>
  <path d="M9 137a80 80 0 0 1 160 0z" fill="#7f86c4"/>
  <path d="M15 150a28 28 0 0 0 56 0z" fill="#f7941d"/>
  <path d="M466 412a28 28 0 0 0 56 0z" fill="#7f86c4"/>
  <path d="M466 440a28 28 0 0 0 56 0z" fill="#f7941d"/>
</svg>

<svg class="footer-bg" viewBox="0 0 1200 595" aria-hidden="true">
  <polygon points="0,50 42,11 1200,96 1200,595 0,595" fill="#7f86c4"/>
  <polygon points="0,65 44,30 1200,96 1200,595 0,595" fill="#0f0e22"/>
</svg>

<h4 class="f-h" style="left:85px">Quick Links</h4>
<span class="f-link" style="top:2762px">Home</span>
<span class="f-link" style="top:2796px">About</span>
<span class="f-link" style="top:2831px">Products</span>
<span class="f-link" style="top:2865px">Projects</span>
<span class="f-link" style="top:2900px">Contributions</span>
<span class="f-link" style="top:2934px">News</span>
<span class="f-link" style="top:2968px">Privacy</span>

<h4 class="f-h" style="left:367px">Contact Details</h4>
<div class="f-icon" style="top:2767px"><svg width="18" height="14" viewBox="0 0 18 14"><rect x="1" y="1" width="16" height="12" rx="2" fill="none" stroke="#fff" stroke-width="1.6"/><path d="M2 2l7 6 7-6" fill="none" stroke="#fff" stroke-width="1.6"/></svg></div>
<span class="f-label" style="top:2765px">Email:</span>
<span class="f-val" style="top:2792px">hello@copperwrenworks.com</span>
<div class="f-icon" style="top:2853px"><svg width="16" height="16" viewBox="0 0 16 16"><path d="M3 1l3 3-2 2c1 2 3 4 5 5l2-2 3 3-2 3C7 15 1 9 1 3z" fill="#fff"/></svg></div>
<span class="f-label" style="top:2851px">Phone:</span>
<span class="f-val" style="top:2878px">555-014-2290</span>
<div class="f-icon" style="top:2939px"><svg width="16" height="16" viewBox="0 0 16 16"><path d="M3 1l3 3-2 2c1 2 3 4 5 5l2-2 3 3-2 3C7 15 1 9 1 3z" fill="#fff"/></svg></div>
<span class="f-label" style="top:2937px">Phone:</span>
<span class="f-val" style="top:2964px">555-014-2290</span>

<h4 class="f-h" style="left:787px">Subscribe Newsletter</h4>
<p class="f-news">Exercitation ullamco laboris nisi ut aliquip xercitation ullamco</p>
<div class="f-input">Email address</div>
<div class="f-send"><svg width="24" height="12" viewBox="0 0 24 12"><path d="M1 6h21M17 1l5 5-5 5" fill="none" stroke="#fff" stroke-width="2"/></svg></div>
<div class="social" style="left:787px"><i></i></div>
<div class="social" style="left:849px"><i></i></div>
<div class="social" style="left:910px"><i></i></div>
<div class="social" style="left:972px"><i></i></div>

<div class="rule"></div>
<p class="copy">Copyright © 2023 CopperWren Works, LLC</p>

</body>
</html>
```